Poster for mountain bike and trail run competition

I am looking for a poster design for a charitable mountain bike and trail run race. It should be something fun, colorful, which can attract participants. The area in which the competition takes place is dominated by hills and by the Nera river which has a beautiful gorge.. I am attaching some of our previous (poorly designed) posters. The poster should have a place where I can add the sponsor logos, which I will do by myself, in the following months.
Text:
Headline: "Poiana Tulvei Mountain Bike and Trail Run Race"
small headline: "Editia a-6a"
small headline: "Sasca Romana, 10-11 IUNIE 2023"
other text:
"10 IUNIE - Concurs Mountain Bike & Concert
11 IUNIE - Concurs Trail Run"
text for enrollments: "inscrieri pe www.brelvacros.ro"

Thanks

• a space where I can add sponsor logos, editable file to be provided (AI, photoshop or corel)

```html
<!DOCTYPE html>
<html lang="ro">
<head>
<meta charset="utf-8">
<title>Poiana Tulvei Mountain Bike &amp; Trail Run Race</title>
<link rel="stylesheet" href="https://fonts.googleapis.com/css2?family=Anton&family=Poppins:wght@500;600;700;800&display=swap">
<style>
  :root {
    --page: #f1f1f1;
    --sky-light: #fde6c9;
    --sky-mid: #fbd3a2;
    --sun-orange: #f4a44a;
    --rust: #b8532d;
    --maroon: #6b1f35;
    --plum: #3f1329;
    --plum-deep: #34101f;
    --accent: #f6a83b;
    --white: #ffffff;
    --logo-green: #6b7a5a;
  }
  * { margin: 0; padding: 0; box-sizing: border-box; }
  html, body { width: 1200px; height: 3355px; overflow: hidden; }
  body { background: var(--page); position: relative; font-family: "Poppins", sans-serif; }

  .poster {
    position: absolute; left: 50px; top: 899px;
    width: 1100px; height: 1557px;
    background: var(--white);
    overflow: hidden;
    box-shadow: 0 18px 50px rgba(0,0,0,.25);
  }
  .poster__sky {
    position: absolute; inset: 0 0 auto 0; height: 1360px;
    background: linear-gradient(180deg, var(--sky-light) 0%, var(--sky-mid) 30%, var(--sun-orange) 45%, var(--plum) 62%, var(--plum) 100%);
  }
  .poster__scene {
    position: absolute; left: 0; top: 600px; width: 1100px; height: 420px;
    background:
      radial-gradient(ellipse 60% 40% at 45% 20%, rgba(253,230,201,.6), transparent 70%),
      linear-gradient(180deg, var(--sun-orange) 0%, var(--rust) 35%, var(--maroon) 60%, var(--plum) 100%);
  }

  .org {
    position: absolute; top: 66px; left: 0; width: 100%;
    display: flex; justify-content: center; align-items: center; gap: 16px;
    color: var(--logo-green);
  }
  .org__mark { width: 44px; height: 44px; border: 3px solid var(--logo-green); }
  .org__name { font-weight: 600; font-size: 28px; line-height: 1.05; text-align: center; }

  .headline { position: absolute; left: 0; width: 100%; text-align: center; font-family: "Anton", sans-serif; text-transform: uppercase; letter-spacing: -1px; line-height: 1; }
  .headline--place { top: 150px; font-size: 132px; color: var(--plum); }
  .headline--sport {
    top: 285px; font-size: 150px;
    background: linear-gradient(180deg, var(--maroon) 0%, var(--rust) 55%, var(--accent) 100%);
    -webkit-background-clip: text; background-clip: text; color: transparent;
  }
  .headline--race { top: 440px; font-size: 118px; color: var(--maroon); }

  .edition { position: absolute; top: 582px; width: 100%; text-align: center; font-weight: 800; font-size: 60px; color: var(--plum-deep); text-transform: uppercase; }

  .venue { position: absolute; top: 1015px; width: 100%; text-align: center; font-weight: 600; font-size: 50px; color: var(--accent); text-transform: uppercase; }
  .dates { position: absolute; top: 1068px; width: 100%; text-align: center; font-weight: 600; font-size: 56px; color: var(--white); }
  .dates__year { color: var(--accent); }

  .schedule { position: absolute; top: 1150px; width: 100%; display: flex; flex-direction: column; align-items: center; gap: 10px; }
  .schedule__item {
    border: 3px solid var(--accent); border-radius: 10px;
    padding: 4px 26px; font-weight: 500; font-size: 32px; color: var(--white); text-transform: uppercase;
  }
  .schedule__day { color: var(--accent); }

  .enroll { position: absolute; top: 1290px; width: 100%; text-align: center; font-weight: 500; font-size: 27px; color: var(--white); }
  .enroll__link { color: var(--accent); }

  .poster__edge { position: absolute; left: 0; top: 1340px; width: 1100px; height: 40px; }
  .sponsors { position: absolute; left: 0; bottom: 0; width: 1100px; height: 190px; background: var(--white); }
</style>
</head>
<body>
  <div class="poster">
    <div class="poster__sky"></div>
    <div class="poster__scene" role="img" aria-label="Illustration: runners and a mountain biker silhouetted on hills with pine trees, river gorge and sunset"></div>

    <div class="org">
      <span class="org__mark"></span>
      <span class="org__name">Clubul Sportiv<br>Valea Brelvei</span>
    </div>

    <h1>
      <span class="headline headline--place">Poiana Tulvei</span>
      <span class="headline headline--sport">Mountain Bike</span>
      <span class="headline headline--race">&amp; Trail Run Race</span>
    </h1>
    <p class="edition">Editia a-6a</p>

    <p class="venue">Sasca Romana</p>
    <p class="dates">10–11 IUNIE <span class="dates__year">2023</span></p>

    <div class="schedule">
      <p class="schedule__item"><span class="schedule__day">10 Iunie -</span> Concurs Mountain Bike &amp; Concert</p>
      <p class="schedule__item"><span class="schedule__day">11 Iunie -</span> Concurs Trail Run</p>
    </div>

    <p class="enroll">Text for enrollments: <span class="enroll__link">"inscrieri pe www.brelvacros.ro"</span></p>

    <svg class="poster__edge" viewBox="0 0 1100 40" preserveAspectRatio="none">
      <path fill="#ffffff" d="M0 24 L20 18 L34 26 L50 14 L66 22 L84 16 L100 25 L118 12 L136 23 L152 17 L170 26 L190 15 L206 22 L224 13 L242 24 L260 18 L278 27 L296 14 L314 21 L332 16 L350 25 L370 12 L388 22 L406 17 L424 26 L442 15 L460 23 L478 18 L496 27 L514 13 L532 22 L550 16 L568 25 L586 14 L604 21 L622 17 L640 26 L658 12 L676 23 L694 18 L712 25 L730 15 L748 22 L766 16 L784 27 L802 13 L820 21 L838 18 L856 25 L874 14 L892 23 L910 17 L928 26 L946 12 L964 22 L982 16 L1000 25 L1018 15 L1036 22 L1054 18 L1072 26 L1088 14 L1100 20 L1100 40 L0 40 Z"/>
    </svg>
    <div class="sponsors" aria-label="Sponsor logos area"></div>
  </div>
</body>
</html>
```